Referral card

We recently had a new logo designed for our company. We are a dental office and would like to have a card designed that we would hand out to patients when asking them to refer friends and family to our office.

5"x7" double-sided card

Text:

title:
From Our Family to Yours

body:
The highest compliment you could give us is to refer your friends and family to our care. Each time you refer a friend or family member to Tamberlin Dental Center you will receive a $10 gift card upon completion of your friend or family member's first visit. It is our way of saying thank you for your trust and confidence in us!

info:
5214 SE Corwick Ave
Silverdale, WA 98471
(360)481-7724
www.tamberlindentalcenter-example.net

We would like the logo present on both the front and back of the card. Possibly also having a photo or two of a smiling face/smiling couple/smiling family would also be good. We are trying to get our brand out there a little more, so having the back of the card have a large logo would be preferred.

Three files uploaded. One has all of the different logo orientations, the other two show the color and styles we like best.

Requirements
Must have
• title, text, and info per the task description
• logo on front and back. photo of smiling faces.

```html
<!DOCTYPE html>
<html lang="en">
<head>
<meta charset="utf-8">
<title>Tamberlin Dental Center – Referral Card</title>
<link rel="stylesheet" href="https://fonts.googleapis.com/css2?family=Arimo:wght@400;700&family=Tinos:wght@400;700&family=Allura&display=swap">
<style>
  :root {
    --page: #2a2a2a;
    --paper: #ffffff;
    --paper-shade: #eef2f6;
    --navy: #2e4d6b;
    --navy-deep: #233d57;
    --brand-blue: #3a6894;
    --leaf: #7d9b3c;
    --leaf-light: #a9c65a;
    --text-dark: #2b3440;
    --white: #ffffff;
  }
  * { box-sizing: border-box; margin: 0; padding: 0; }
  html, body { width: 720px; height: 1200px; overflow: hidden; }
  body {
    background: var(--page);
    font-family: "Arimo", Arial, sans-serif;
    position: relative;
  }
  .card {
    position: absolute;
    left: 30px;
    width: 660px;
    height: 470px;
    background: linear-gradient(160deg, var(--paper) 40%, var(--paper-shade));
    overflow: hidden;
  }
  .card--front { top: 60px; }
  .card--back { top: 660px; }

  .photo {
    position: absolute;
    background: linear-gradient(135deg, #dfe6ee 0%, #c9b3a0 45%, #9a7a62 70%, #e9edf2 100%);
  }
  .card--front .photo { right: 0; top: 0; width: 300px; height: 330px; }
  .card--back .photo {
    left: 330px; top: 125px; width: 310px; height: 230px;
    background: linear-gradient(120deg, #e8ecf0 0%, #c8a58a 35%, #b0b8c2 60%, #d8c19f 85%, #eef1f4 100%);
  }

  .wave { position: absolute; left: 0; top: 0; width: 660px; height: 470px; }

  .brand {
    position: absolute;
    display: flex;
    align-items: center;
    gap: 10px;
    color: var(--brand-blue);
    font-family: "Arimo", Arial, sans-serif;
    font-weight: 400;
    white-space: nowrap;
  }
  .brand__dot {
    border-radius: 50%;
    background: var(--brand-blue);
    flex: none;
  }
  .card--front .brand { left: 58px; top: 36px; font-size: 20px; }
  .card--front .brand__dot { width: 16px; height: 16px; }
  .card--back .brand { right: 26px; top: 62px; font-size: 23px; }
  .card--back .brand__dot { width: 20px; height: 20px; }

  .title {
    position: absolute;
    left: 30px; top: 78px;
    color: var(--brand-blue);
    font-weight: 700;
    font-size: 37px;
    line-height: 1;
    letter-spacing: -0.5px;
  }
  .title__to {
    display: block;
    margin: 4px 0 0 120px;
    font-size: 26px;
  }
  .title__yours {
    font-family: "Allura", cursive;
    font-weight: 400;
    color: var(--leaf);
    font-size: 62px;
    margin-left: 4px;
  }

  .info { position: absolute; left: 52px; top: 206px; color: var(--brand-blue); }
  .info__name { font-weight: 700; font-size: 19px; letter-spacing: 0.2px; }
  .info__address {
    display: flex; align-items: center; gap: 8px;
    margin-top: 5px; font-size: 12px; line-height: 1.3; color: var(--text-dark);
  }
  .info__phone { margin-top: 8px; font-weight: 700; font-size: 26px; color: var(--navy); }
  .info__web { font-weight: 700; font-size: 12px; color: var(--navy); }

  .offer {
    position: absolute; left: 44px; top: 380px; color: var(--white);
  }
  .offer__lead { font-weight: 700; font-size: 19px; }
  .offer__amount { color: var(--leaf-light); font-size: 30px; margin-left: 4px; }
  .offer__note { font-weight: 700; font-size: 12.5px; line-height: 1.35; margin-top: 4px; }

  .message {
    position: absolute; left: 30px; top: 70px; width: 285px;
    font-family: "Tinos", "Times New Roman", serif;
    font-size: 18.5px; line-height: 1.22; color: var(--text-dark);
    text-align: justify;
  }
  .message p + p { margin-top: 8px; }
  .message strong { color: var(--navy); }
  .message__amount { font-size: 26px; font-weight: 700; color: var(--navy); }

  .contact { position: absolute; left: 118px; top: 410px; color: var(--white); }
  .contact__phone { font-weight: 700; font-size: 26px; }
  .contact__web { font-weight: 700; font-size: 12px; }
  .contact__address {
    position: absolute; right: 30px; top: 392px;
    color: var(--white); font-weight: 700; font-size: 13px;
  }
</style>
</head>
<body>

<section class="card card--front" aria-label="Referral card front">
  <div class="photo" role="img" aria-label="Photo of a smiling young woman"></div>
  <svg class="wave" viewBox="0 0 660 470" aria-hidden="true">
    <path d="M0 345 C 200 330, 430 290, 660 205 L660 470 L0 470 Z" fill="var(--white)"/>
    <path d="M0 360 C 220 345, 440 300, 660 225" fill="none" stroke="var(--leaf)" stroke-width="5"/>
    <path d="M0 372 C 230 358, 450 315, 660 245 L660 470 L0 470 Z" fill="var(--navy)"/>
    <path d="M0 390 C 240 375, 460 335, 660 270" fill="none" stroke="var(--navy-deep)" stroke-width="14" opacity="0.5"/>
  </svg>

  <div class="brand"><span class="brand__dot"></span>Tamberlin Dental Center</div>

  <h1 class="title">From Our Family<span class="title__to">To <span class="title__yours">Yours</span></span></h1>

  <div class="info">
    <div class="info__name">TAMBERLIN DENTAL CENTER</div>
    <div class="info__address">
      <svg width="14" height="14" viewBox="0 0 14 14" aria-hidden="true"><circle cx="7" cy="7" r="6" fill="var(--brand-blue)"/></svg>
      <span>5214 SE Corwick Ave<br>Silverdale, WA 98471</span>
    </div>
    <div class="info__phone">(360)481-7724</div>
    <div class="info__web">www.tamberlindentalcenter-example.net</div>
  </div>

  <div class="offer">
    <div class="offer__lead">Receive GIFT CARD <span class="offer__amount">$10</span></div>
    <div class="offer__note">Upon completion of your friend or family member's first visit.<br>It is our way of saying thank you for your trust and confidence in us!</div>
  </div>
</section>

<section class="card card--back" aria-label="Referral card back">
  <div class="photo" role="img" aria-label="Photo of a smiling family of four"></div>
  <svg class="wave" viewBox="0 0 660 470" aria-hidden="true">
    <path d="M0 380 C 220 370, 440 345, 660 300 L660 470 L0 470 Z" fill="var(--white)"/>
    <path d="M0 388 C 220 378, 440 352, 660 310" fill="none" stroke="var(--leaf)" stroke-width="5"/>
    <path d="M0 398 C 230 388, 450 362, 660 322 L660 470 L0 470 Z" fill="var(--navy)"/>
  </svg>

  <div class="brand"><span class="brand__dot"></span>Tamberlin Dental Center</div>

  <div class="message">
    <p>The <strong>highest compliment</strong> you could give us is to refer your friends and family to our care. Each time you refer a friend or family member to <strong>Tamberlin Dental Center</strong> you will receive a</p>
    <p><span class="message__amount">$10</span> <strong>GIFT CARD</strong> upon completion of your friend or family member's first visit. It is our way of saying <strong>THANK YOU</strong> for your trust and confidence in us!</p>
  </div>

  <div class="contact">
    <div class="contact__phone">(360)481-7724</div>
    <div class="contact__web">www.tamberlindentalcenter-example.net</div>
  </div>
  <div class="contact__address">5214 SE Corwick Ave Silverdale, WA 98471</div>
</section>

</body>
</html>
```